Brindle-Oak.com -> We need someone to design a homepage [For Mobile]

We need a graphic design of our homepage for mobile, which will include login and signup. It's only the design we need, we would take care of the coding, so if you're a good designer you're welcome to participate. The Login & Registration page contain a few fields. Login --> Username & Password & Forgot my Password. Registration --> Email, Username, Password. Needs to be a clean design.[Registration in a different page, Login and Homepage in the same one]
Updates

Project Deadline Extended Reason: We're going to consider what we got so far and allow others to submit more designs as well, the final deadline would be this week, we won't extend it again. Added Saturday, December 20, 2014

Project Deadline Extended Reason: Very sorry, we just got more than expected designs and we want to go over all of them in order to make a proper decision - we would extend the project until the 1st of January 2015, this is definitely a FINAL date. Added Friday, December 26, 2014

Industry/Entity Type

Graphic Design

Number of Pages Required

2 page

Requirements
Must have
• * Enclosed our logo to include with the design.
• * Add the following text as well
• WANT TO EARN EXTRA MONEY?
• WITH BRINDLE-OAK.COM YOU CAN!
• BRINDLE-OAK.COM. IT'S AS EASY AS 1, 2, 3.
• (1) Register (2) Earn & Win Coins (3) Redeem Coins
• * It must have "Login" and "Register" buttons on the home page.
Nice to have
• [Note: Also to make it easier for you, enclosed a screenshot of the main page in a desktop (PC) view.]

```html
<!DOCTYPE html>
<html lang="en">
<head>
<meta charset="utf-8">
<title>Brindle-Oak.com – Mobile Home</title>
<link rel="stylesheet" href="https://fonts.googleapis.com/css2?family=Itim&family=Lato:wght@400;700&display=swap">
<style>
  :root {
    --page-bg: #e6e6e6;
    --sky-top: #232b38;
    --sky-mid: #6f87a4;
    --sky-glow: #b5c6dd;
    --sky-bottom: #1b212d;
    --panel: rgba(32, 34, 42, 0.78);
    --accent-green: #7cc242;
    --coin-light: #d6f500;
    --coin-mid: #8fb000;
    --coin-dark: #3d4a00;
    --field-bg: #f4f4f4;
    --field-ring: #c9ccd2;
    --field-text: #4a4d55;
    --icon-blue: #4a6aae;
    --social-blue: #3d5c9e;
    --social-blue-dark: #324d88;
    --white: #ffffff;
  }
  * { box-sizing: border-box; margin: 0; padding: 0; }
  html, body { width: 1120px; height: 1200px; overflow: hidden; background: var(--page-bg); }
  .screen {
    position: absolute; left: 209px; top: 0; width: 702px; height: 1200px; overflow: hidden;
    background: linear-gradient(180deg, var(--sky-top) 0%, var(--sky-mid) 32%, var(--sky-mid) 46%, var(--sky-glow) 56%, var(--sky-mid) 64%, #3a4760 80%, var(--sky-bottom) 100%);
    font-family: "Lato", sans-serif;
  }
  .brand {
    position: absolute; top: 72px; left: 0; width: 100%;
    display: flex; justify-content: center; align-items: center; gap: 16px;
  }
  .brand-dot { width: 46px; height: 46px; border-radius: 50%; background: var(--accent-green); }
  .brand-name { font-family: "Lato", sans-serif; font-weight: 700; font-size: 44px; color: var(--accent-green); }
  .coin {
    position: absolute; left: 83px; top: 396px; width: 510px; height: 510px; border-radius: 50%;
    background: radial-gradient(ellipse at 50% 62%, var(--coin-light) 0%, var(--coin-mid) 35%, var(--coin-dark) 85%);
    opacity: 0.95;
  }
  .panel {
    position: absolute; left: 81px; width: 545px; border-radius: 18px; background: var(--panel);
  }
  .panel-intro { top: 228px; height: 468px; }
  .panel-login { top: 729px; height: 353px; }
  .headline {
    position: absolute; top: 248px; left: 0; width: 100%; text-align: center;
    font-family: "Itim", cursive; font-size: 44px; color: var(--accent-green);
  }
  .tagline {
    position: absolute; top: 310px; left: 0; width: 100%; text-align: center;
    font-size: 28px; color: var(--white);
  }
  .field {
    position: absolute; left: 103px; width: 493px; height: 72px; border-radius: 36px;
    background: var(--field-bg); border: 5px solid var(--field-ring);
    box-shadow: 0 2px 4px rgba(0,0,0,0.3);
    display: flex; align-items: center; padding-left: 24px; gap: 26px;
    font-size: 18px; color: var(--field-text);
  }
  .field svg { width: 26px; height: 26px; flex: none; }
  .social-login {
    position: absolute; left: 185px; top: 975px; width: 322px; height: 63px; border-radius: 4px;
    background: var(--social-blue); display: flex; align-items: center; overflow: hidden;
  }
  .social-mark { width: 60px; height: 100%; background: var(--social-blue-dark); }
  .social-label { flex: 1; text-align: center; color: var(--white); font-size: 26px; }
</style>
</head>
<body>
<main class="screen">
  <div class="brand">
    <span class="brand-dot"></span>
    <span class="brand-name">brindle-oak</span>
  </div>

  <div class="coin" role="img" aria-label="Large glossy green coin with a dollar sign"></div>

  <section class="panel panel-intro"></section>
  <h1 class="headline">Want To Earn Extra Money?</h1>
  <p class="tagline">With Brindle-Oak.com. It's Easy As 1.2.3.</p>

  <div class="field" style="top:384px">
    <svg viewBox="0 0 24 24"><circle cx="12" cy="7" r="5" fill="var(--accent-green)"/><path d="M3 22c0-5 4-8 9-8s9 3 9 8z" fill="var(--accent-green)"/></svg>
    Register
  </div>
  <div class="field" style="top:477px">
    <svg viewBox="0 0 24 24"><path d="M1 9l11-5 11 5-11 5z" fill="var(--accent-green)"/><path d="M6 12v5c3 2 9 2 12 0v-5l-6 3z" fill="var(--accent-green)"/></svg>
    Earn &amp; Win coins
  </div>
  <div class="field" style="top:570px">
    <svg viewBox="0 0 24 24"><path d="M5 3h14M5 8h14M5 3h5a5 5 0 0 1 0 10H6l9 9" stroke="var(--accent-green)" stroke-width="2.4" fill="none"/></svg>
    Reedem Coins
  </div>

  <section class="panel panel-login"></section>
  <div class="field" style="top:765px">
    <svg viewBox="0 0 24 24"><circle cx="12" cy="7" r="5" fill="var(--icon-blue)"/><path d="M3 22c0-5 4-8 9-8s9 3 9 8z" fill="var(--icon-blue)"/></svg>
    Username@mailbox.com
  </div>
  <div class="field" style="top:861px">
    <svg viewBox="0 0 24 24"><path d="M7 11V7a5 5 0 0 1 10 0v4" stroke="var(--icon-blue)" stroke-width="2.4" fill="none"/><rect x="4" y="11" width="16" height="12" rx="2" fill="var(--icon-blue)"/></svg>
    Password
  </div>

  <a class="social-login">
    <span class="social-mark"></span>
    <span class="social-label">Login with Circlenet</span>
  </a>
</main>
</body>
</html>
```